Olive Oil label for bottle 0.5l approx. 10x12 cm

I am running a Spa hotel in Bavaria (logo attached) and my family lives in Greece (Bavarian and Greek flag have the same colors). They produce organic olive oil first cold pressed extra virgin. I would need a label for 0,5 liter bottles to reach them out to my guests and they should see the high quality of the olive oil and the family connection Spa-hotel Bavaria to family in Greece. The name of the family is Merovski, the hotel is called Talgrund, the olive oil comes from Greece/Argolis/Kranidi. The name of the small olive company is Dorin Herons. There should be a space for the best before date and the organic control number (handwritten) . The hotel logo is not mandatory. Should look nice 😉

```html
<!DOCTYPE html>
<html lang="en">
<head>
<meta charset="utf-8">
<title>Merovski Extra Virgin Olive Oil Labels</title>
<link rel="stylesheet" href="https://fonts.googleapis.com/css2?family=Allura&family=Merriweather:wght@400;700&display=swap">
<style>
  :root {
    --backdrop: #e9eef4;
    --label-light: #fbfbfc;
    --label-mid: #eeeff1;
    --label-edge: #c9cbce;
    --aegean-blue: #1d4fa8;
    --ink-blue: #2a57b3;
    --branch-tone: #c9d6ee;
    --ink-dark: #1a1a1a;
    --ink-grey: #555a62;
    --rule: #2b2b2b;
    --white: #ffffff;
  }
  * { box-sizing: border-box; margin: 0; padding: 0; }
  html, body {
    width: 1200px;
    height: 800px;
    overflow: hidden;
    background: var(--backdrop);
  }
  .canvas { position: relative; width: 1200px; height: 800px; }

  .label {
    position: absolute;
    top: 25px;
    width: 268px;
    height: 750px;
    background: linear-gradient(90deg,
      var(--label-edge) 0%, var(--label-mid) 14%, var(--label-light) 40%,
      var(--label-light) 62%, var(--label-mid) 84%, var(--label-edge) 100%);
    font-family: "Merriweather", Georgia, serif;
    color: var(--ink-dark);
  }
  .label--story { left: 120px; padding: 40px 30px 0; }
  .label--front { left: 466px; text-align: center; }
  .label--facts { left: 812px; padding: 34px 28px 0; }

  /* Front label */
  .front__top-band {
    position: absolute; left: 46px; right: 14px; top: 0; height: 20px;
    background: var(--aegean-blue); border-radius: 0 0 3px 3px;
  }
  .front__origin {
    position: absolute; top: 34px; left: 0; right: 0;
    font-weight: 700; font-size: 17px; line-height: 20px; color: var(--aegean-blue);
  }
  .front__brand {
    position: absolute; top: 220px; left: 0; right: 0;
    font-family: "Allura", cursive; font-weight: 400;
    font-size: 78px; line-height: 84px; color: var(--ink-blue);
  }
  .front__branch { position: absolute; left: 72px; top: 338px; width: 137px; height: 150px; }
  .front__grade {
    position: absolute; left: 58px; top: 626px; width: 165px; height: 30px;
    background: var(--aegean-blue); color: var(--white);
    font-weight: 700; font-size: 15px; line-height: 30px; border-radius: 2px;
  }
  .front__process {
    position: absolute; top: 668px; left: 0; right: 0;
    font-weight: 700; font-size: 14px; line-height: 16px;
  }
  .front__volume {
    position: absolute; top: 710px; left: 0; right: 0;
    font-weight: 700; font-size: 17px; line-height: 22px;
  }

  /* Story label */
  .story__brand {
    font-family: "Allura", cursive; font-size: 48px; line-height: 52px;
    color: var(--ink-blue);
  }
  .story__heading {
    margin: 24px 0 18px; font-size: 13px; font-weight: 700; color: var(--aegean-blue);
  }
  .story__text {
    font-size: 11.5px; line-height: 19px; color: var(--ink-grey); margin-bottom: 14px;
  }
  .story__footer {
    position: absolute; left: 24px; right: 24px; bottom: 86px;
    padding: 8px 0; border-top: 2px solid var(--branch-tone); border-bottom: 2px solid var(--branch-tone);
    font-size: 11px; font-weight: 700; color: var(--aegean-blue); text-align: center;
  }

  /* Facts label */
  .facts__table { border: 2px solid var(--rule); padding: 6px 8px; font-size: 11px; line-height: 17px; }
  .facts__title { font-size: 17px; font-weight: 700; line-height: 22px; border-bottom: 5px solid var(--rule); padding-bottom: 4px; margin-bottom: 4px; }
  .facts__row { display: flex; justify-content: space-between; border-bottom: 1px solid var(--rule); }
  .facts__row--strong { font-weight: 700; border-bottom-width: 3px; }
  .facts__row:last-child { border-bottom: none; }
  .facts__meta { margin-top: 16px; font-size: 11px; line-height: 18px; color: var(--ink-grey); }
  .facts__meta-row { display: flex; align-items: center; gap: 10px; }
  .facts__badge { width: 34px; height: 34px; border-radius: 50%; background: var(--branch-tone); flex: none; }
  .facts__field { margin-top: 14px; font-size: 11px; font-weight: 700; color: var(--aegean-blue); }
  .facts__line { display: block; height: 22px; border-bottom: 1px solid var(--ink-grey); }
</style>
</head>
<body>
  <main class="canvas">
    <section class="label label--story">
      <p class="story__brand">Merovski</p>
      <h2 class="story__heading">From Kranidi to Talgrund</h2>
      <p class="story__text">Grown by the Merovski family in Kranidi, Argolis, our olives are picked early and first cold pressed within hours.</p>
      <p class="story__text">Each bottle travels from our grove in Greece to Spa Hotel Talgrund in Bavaria, linking two family homes that share the same blue and white colours.</p>
      <p class="story__text">Enjoy it raw over salads, bread and grilled fish.</p>
      <p class="story__footer">Dorin Herons · Kranidi, Greece</p>
    </section>

    <section class="label label--front">
      <div class="front__top-band"></div>
      <p class="front__origin">Authentic Greek<br>Extra virgin olive oil</p>
      <h1 class="front__brand">Merovski</h1>
      <svg class="front__branch" role="img" aria-label="Line illustration of an olive branch with olives" viewBox="0 0 137 150">
        <ellipse cx="68" cy="75" rx="58" ry="70" fill="var(--branch-tone)" opacity="0.55"/>
      </svg>
      <div class="front__grade">SPECIAL SELECT</div>
      <p class="front__process">Early Harvest<br>First Cold Pressed</p>
      <p class="front__volume">Net Wt. 500ml</p>
    </section>

    <section class="label label--facts">
      <div class="facts__table">
        <p class="facts__title">Nutrition Facts</p>
        <div class="facts__row facts__row--strong"><span>Serving size 1 tbsp</span><span>(15 ml)</span></div>
        <div class="facts__row facts__row--strong"><span>Calories</span><span>120</span></div>
        <div class="facts__row"><span>Total Fat</span><span>14 g</span></div>
        <div class="facts__row"><span>Saturated Fat</span><span>2 g</span></div>
        <div class="facts__row"><span>Trans Fat</span><span>0 g</span></div>
        <div class="facts__row"><span>Sodium</span><span>0 mg</span></div>
        <div class="facts__row"><span>Protein</span><span>0 g</span></div>
      </div>
      <div class="facts__meta">
        <div class="facts__meta-row">
          <p>Ingredients: organic extra virgin olive oil.</p>
          <span class="facts__badge"></span>
        </div>
        <p>Origin: Kranidi, Argolis, Greece</p>
        <p>Store cool and dark.</p>
      </div>
      <p class="facts__field">Best before:<span class="facts__line"></span></p>
      <p class="facts__field">Organic control no.:<span class="facts__line"></span></p>
    </section>
  </main>
</body>
</html>
```